KRTLO Promotion Flyer to raise money and communicate our goals

We need a flyer that promotes our organization. We are a 501(c)3 trying to raise money for Arts, Education and Entrepreneurship in our small town.

We promote a social events that improve qualtiy of life and educate people on how to start and expand businesses. Our goal is to make downtown an active and thriving place with many things for people to do and enjoy as well as create a favorable place for business.

Target Market(s)

Wealthy donors and Organizations with cash

Industry/Entity Type

Education

Colors

Designer to choose colors to be used in the design.

Requirements
Must have
• Eye catching graphics and look very professional
• Should appeal to men and women
Nice to have
• Make use of any known psychological colors and fonts etc... that appeal to philanthropic people
Should not have
• Should not be complicated or confusing

```html
<!DOCTYPE html>
<html lang="en">
<head>
<meta charset="utf-8">
<title>KRTLO Flyer</title>
<link href="https://fonts.googleapis.com/css2?family=Source+Sans+3:wght@400;600;700&family=Great+Vibes&display=swap" rel="stylesheet">
<style>
:root{
  --ink:#3a3a3a;
  --blue:#1fa9e1;
  --blue-light:#b9e6f8;
  --green:#8cc63f;
  --pink:#e2337a;
  --panel:#f1f1f1;
  --white:#ffffff;
  --forest-dark:#3d4a2c;
  --forest-mid:#7d8a52;
  --forest-light:#d9d5b0;
}
*{margin:0;padding:0;box-sizing:border-box}
html,body{width:1010px;height:1200px;overflow:hidden;background:#fff}
.flyer{position:relative;width:1010px;height:1200px;font-family:"Source Sans 3",Arial,sans-serif;color:var(--ink)}
.backdrop{position:absolute;inset:0}
.brand{position:absolute;left:48px;top:520px;display:flex;align-items:center;gap:14px}
.brand-square{width:34px;height:34px;background:var(--blue)}
.brand-name{font-size:52px;font-weight:700;color:var(--blue);letter-spacing:2px}
.intro{position:absolute;left:39px;top:640px;width:546px;font-size:17px;line-height:19.7px;text-align:justify}
.pillars{position:absolute;left:39px;top:757px;width:546px;list-style:none}
.pillar{position:relative;padding-left:28px;font-size:17px;line-height:19.7px;text-align:justify;margin-bottom:20px}
.pillar:nth-child(2){margin-bottom:14px}
.pillar:nth-child(3){margin-bottom:25px}
.pillar-title{color:var(--blue);font-weight:600}
.tick{position:absolute;left:0;top:4px;width:16px;height:16px}
.appeal{position:absolute;left:668px;top:554px;width:323px;font-size:17px;line-height:19.7px;text-align:justify}
.appeal p{margin-bottom:19px}
.donate{position:absolute;left:668px;top:970px;font-family:"Great Vibes",cursive;font-size:34px;color:var(--pink)}
.contact{position:absolute;left:41px;top:1104px;color:var(--white);font-weight:700;font-size:19.5px;line-height:32px}
</style>
</head>
<body>
<div class="flyer">
  <svg class="backdrop" width="1010" height="1200" viewBox="0 0 1010 1200">
    <defs>
      <linearGradient id="forest" x1="0" y1="0" x2="0" y2="1">
        <stop offset="0" stop-color="var(--forest-dark)"/>
        <stop offset="0.35" stop-color="var(--forest-light)"/>
        <stop offset="0.7" stop-color="var(--forest-mid)"/>
        <stop offset="1" stop-color="#5d6b2a"/>
      </linearGradient>
      <linearGradient id="swoosh" x1="0" y1="0" x2="1" y2="0">
        <stop offset="0" stop-color="var(--blue-light)"/>
        <stop offset="1" stop-color="var(--blue)"/>
      </linearGradient>
      <linearGradient id="hall" x1="0" y1="0" x2="0" y2="1">
        <stop offset="0" stop-color="#a9cbe6"/>
        <stop offset="0.55" stop-color="#d8c9b3"/>
        <stop offset="1" stop-color="#9c8a64"/>
      </linearGradient>
    </defs>
    <rect x="0" y="0" width="1010" height="470" fill="url(#forest)" role="img" aria-label="Photo of a sunlit pine forest"/>
    <path d="M0,460 C250,360 480,322 720,318 L860,330 L1010,392 L1010,1200 L0,1200 Z" fill="var(--white)"/>
    <rect x="624" y="326" width="386" height="874" fill="var(--panel)"/>
    <path d="M0,498 C220,400 470,332 720,318" fill="none" stroke="url(#swoosh)" stroke-width="16"/>
    <path d="M940,360 L1010,392" stroke="var(--blue)" stroke-width="3"/>
    <circle cx="839" cy="370" r="122" fill="var(--white)"/>
    <circle cx="839" cy="370" r="112" fill="url(#hall)" role="img" aria-label="Photo of the open-sided town pavilion"/>
    <polygon points="0,1053 1010,1200 0,1200" fill="var(--green)"/>
    <polygon points="1010,1050 1010,1200 760,1168" fill="var(--pink)"/>
    <path d="M700,1168 C820,1140 930,1090 1010,1028" fill="none" stroke="url(#swoosh)" stroke-width="12"/>
  </svg>

  <div class="brand">
    <span class="brand-square"></span>
    <span class="brand-name">KRTLO</span>
  </div>

  <p class="intro">The Cedar Hollow Small Business Association (KRTLO) is a local leader in the areas of Arts, Education and Entrepreneurship and is working diligently to promote Cedar Hollow and revitalize our downtown. When you become an KRTLO Member, you will be a part of the citywide work that the KRTLO does every day to improve the lives of citizens of Cedar Hollow:</p>

  <ul class="pillars">
    <li class="pillar"><svg class="tick" viewBox="0 0 16 16"><circle cx="8" cy="8" r="6.5" fill="none" stroke="var(--blue)" stroke-width="1.4"/><path d="M5,8 L7.3,10.2 L11,6" fill="none" stroke="var(--blue)" stroke-width="1.6"/></svg><span class="pillar-title">WE PROMOTE</span><br>Cedar Hollow Hotels, Shopping and Events that make Cedar Hollow a pleasant, exciting and prosperous place to live.</li>
    <li class="pillar"><svg class="tick" viewBox="0 0 16 16"><circle cx="8" cy="8" r="6.5" fill="none" stroke="var(--blue)" stroke-width="1.4"/><path d="M5,8 L7.3,10.2 L11,6" fill="none" stroke="var(--blue)" stroke-width="1.6"/></svg><span class="pillar-title">WE PROVIDE</span><br>training and resources to anyone interested Arts, Education and Entrepreneurship.</li>
    <li class="pillar"><svg class="tick" viewBox="0 0 16 16"><circle cx="8" cy="8" r="6.5" fill="none" stroke="var(--blue)" stroke-width="1.4"/><path d="M5,8 L7.3,10.2 L11,6" fill="none" stroke="var(--blue)" stroke-width="1.6"/></svg><span class="pillar-title">WE HELP</span><br>entrepreneur’s start and grow their businesses in a tax efficient and appropriate way.</li>
    <li class="pillar"><svg class="tick" viewBox="0 0 16 16"><circle cx="8" cy="8" r="6.5" fill="none" stroke="var(--blue)" stroke-width="1.4"/><path d="M5,8 L7.3,10.2 L11,6" fill="none" stroke="var(--blue)" stroke-width="1.6"/></svg><span class="pillar-title">WE WORK</span> with all levels of local government to promote our community and create a fertile environment for growth.</li>
  </ul>

  <div class="appeal">
    <p>Every day, we look for ways to help our local businesses grow and expand, but we need you by our side.</p>
    <p>As an KRTLO Member, you can help provide training, education and support, and you can give our many businesses a chance to grow and our citizens the opportunity to experience big town amenities and events in a small town.</p>
    <p>Members' regular monthly gifts provide a consistent, reliable income stream that allows us to spend less time fundraising—and more time helping our businesses and community.</p>
    <p>Becoming an KRTLO Member is an easy, efficient and tax-deductible way to make a difference for our community all year long.</p>
  </div>
  <div class="donate">Please Donate Today.</div>

  <div class="contact">FOR MORE INFORMATION,<br>e-mail mara@pinegatecpa.com or leo@pinegatecpa.com<br>or logon to CHHUB.com.</div>
</div>
</body>
</html>
```